Bref créative
Stationary (Branding) for Plumbing & Heating Buisness
Dorrick Haines Ltd
Use same font as used in my logo
Dorrick Haines
Unit 8 Larchmoor Ind Est.
Cwmbrellog
Brynhalt
Gwentmere
dorrick@greenvoltaria.co.uk
www.dorrickhaines.com
Looking for complete stationary with A4 letter head, business cards and so on using the logo provided. Modern, clean and eco friendly is the image we are looking for.
The font used in the logo is not final and maybe changed so please ignore that.
Would like to see the logo on the back of the card with spot UV effect.
The font in this logo is not final and may change
plumbing
renewables
heating

```html
<!DOCTYPE html>
<html lang="en">
<head>
<meta charset="utf-8">
<title>Dorrick Haines Ltd — Business Card</title>
<link rel="stylesheet" href="https://fonts.googleapis.com/css2?family=Open+Sans:wght@400;600;700&display=swap">
<style>
  :root {
    --stage: #eceeec;
    --card: #ffffff;
    --ink: #4a4a4a;
    --ink-soft: #8a8a8a;
    --green: #5cb82e;
    --green-deep: #3f8f1c;
    --charcoal: #2f3133;
    --shadow: rgba(0, 0, 0, 0.14);
  }
  * { box-sizing: border-box; margin: 0; padding: 0; }
  html, body { width: 1200px; height: 629px; overflow: hidden; }
  body {
    background: var(--stage);
    font-family: "Open Sans", Arial, sans-serif;
    color: var(--ink);
    position: relative;
  }
  .card {
    position: absolute;
    top: 165px;
    width: 525px;
    height: 300px;
    background: var(--card);
    box-shadow: 0 6px 18px var(--shadow);
    overflow: hidden;
  }
  .card--back { left: 50px; }
  .card--front { left: 625px; }

  /* back */
  .back-web {
    position: absolute;
    left: 34px;
    top: 150px;
    transform: translate(-50%, -50%) rotate(-90deg);
    font-size: 11px;
    letter-spacing: 4px;
    color: var(--ink-soft);
    white-space: nowrap;
  }
  .back-mark {
    position: absolute;
    left: 0; right: 0; top: 128px;
    display: flex; align-items: center; justify-content: center; gap: 10px;
  }
  .mark-dot {
    width: 26px; height: 26px; border-radius: 50%;
    background: var(--green);
    flex: none;
  }
  .back-name { font-size: 24px; font-weight: 700; color: var(--green-deep); }

  /* front */
  .front-brand {
    position: absolute;
    left: 40px; top: 92px;
    display: flex; align-items: center; gap: 10px;
  }
  .front-name {
    font-size: 25px; font-weight: 700; color: var(--green-deep);
    white-space: nowrap;
  }
  .front-person {
    position: absolute; left: 40px; top: 150px;
    font-size: 12px; line-height: 1.55;
  }
  .person-name { color: var(--green); font-weight: 600; font-size: 13px; }
  .address { color: var(--ink); font-size: 11px; margin-top: 6px; }
  .contact {
    position: absolute; left: 290px; top: 150px;
    list-style: none; font-size: 11px; line-height: 1.9;
  }
  .contact li { display: flex; align-items: center; gap: 7px; }
  .contact-icon { width: 10px; height: 10px; background: var(--green); flex: none; }
  .swoosh { position: absolute; left: 0; bottom: 0; width: 525px; height: 70px; }
  .front-web {
    position: absolute; left: 40px; bottom: 4px;
    font-size: 10px; line-height: 14px; letter-spacing: 3px; color: #ffffff;
  }
</style>
</head>
<body>
  <section class="card card--back" aria-label="Card back">
    <p class="back-web">www.dorrickhaines.com</p>
    <div class="back-mark">
      <span class="mark-dot"></span>
      <span class="back-name">Dorrick Haines Ltd</span>
    </div>
  </section>

  <section class="card card--front" aria-label="Card front">
    <div class="front-brand">
      <span class="mark-dot"></span>
      <span class="front-name">Dorrick Haines Ltd.</span>
    </div>
    <div class="front-person">
      <p class="person-name">Dorrick Haines</p>
      <p class="address">Unit 8 Larchmoor Ind Est.<br>Cwmbrellog, Brynhalt, Gwentmere</p>
    </div>
    <ul class="contact">
      <li><span class="contact-icon"></span>01632 960418</li>
      <li><span class="contact-icon"></span>07700 900266</li>
      <li><span class="contact-icon"></span>dorrick@greenvoltaria.co.uk</li>
      <li><span class="contact-icon"></span>www.dorrickhaines.com</li>
    </ul>
    <svg class="swoosh" viewBox="0 0 525 70" preserveAspectRatio="none" aria-hidden="true">
      <path d="M0 34 C160 52 340 46 525 10 L525 22 C340 56 160 62 0 46 Z" fill="var(--green)"/>
      <path d="M0 46 C160 62 340 56 525 22 L525 70 L0 70 Z" fill="var(--charcoal)"/>
    </svg>
    <p class="front-web">www.dorrickhaines.com</p>
  </section>
</body>
</html>
```